Need Help having my business card stand out

I am the owner of Pine Ridge Canine Coaching and would like for my business cards to stand out. I have been trying to keep designing them myself but I can't get what I have in my head on the card. I will try my best to post templates that I like for inspirations. I want something unique but elegant. I don't want in to look cartoony or cheesy. It needs to pop in a pet shop but also in a coffee shop or gym.

Target Market(s)

Dog owners, Married ,No young kids Jr High school kids and up (maybe kids on the way) Executives, Stay at home moms/wives, Small business owners

Industry/Entity Type

Dog Training

Contact Information for Business Card

Trevor Holloway, 555-304-7162, info@pineridgecanine.example, www.pineridgecanine.example

Colors

Designer to choose colors to be used in the design.

Requirements
Must have
• my logo
Should not have
• Cursive lettering

```html
<!DOCTYPE html>
<html lang="en">
<head>
<meta charset="UTF-8">
<title>Pine Ridge Canine Coaching — Business Card</title>
<link rel="stylesheet" href="https://fonts.googleapis.com/css2?family=Montserrat:wght@700&family=Open+Sans:wght@400;700&display=swap">
<style>
  :root {
    --page-bg: #ece8e2;
    --green-bright: #00d200;
    --green-deep: #036d03;
    --green-line: #1fd81f;
    --ink: #0b0b0b;
    --white: #ffffff;
    --ring: #5a5a5a;
    --photo-a: #c9b9a4;
    --photo-b: #6f7a4d;
    --photo-c: #a3543f;
  }
  * { box-sizing: border-box; margin: 0; padding: 0; }
  html, body { width: 1200px; height: 894px; overflow: hidden; }
  body {
    background: var(--page-bg);
    font-family: "Open Sans", Arial, sans-serif;
    position: relative;
  }
  .card {
    position: absolute;
    width: 640px;
    height: 366px;
    display: flex;
    overflow: hidden;
    box-shadow: 0 10px 24px rgba(0,0,0,.22);
  }
  .card-front { left: 60px; top: 50px; }
  .card-back { left: 500px; top: 478px; }

  /* front */
  .portrait {
    width: 42%;
    height: 100%;
    background: linear-gradient(160deg, var(--photo-a) 0%, var(--photo-c) 45%, var(--photo-b) 100%);
  }
  .front-brand {
    flex: 1;
    background: var(--green-bright);
    display: flex;
    align-items: center;
    justify-content: center;
  }
  .brand-seal {
    width: 270px;
    height: 270px;
    border-radius: 50%;
    background: var(--white);
    border: 5px solid var(--ring);
    display: flex;
    align-items: center;
    justify-content: center;
    text-align: center;
    padding: 30px;
  }
  .brand-name {
    font-family: "Open Sans", Arial, sans-serif;
    font-weight: 700;
    color: var(--ink);
    font-size: 30px;
    line-height: 1.15;
  }

  /* back */
  .back-info {
    width: 54%;
    height: 100%;
    background: var(--green-deep);
    padding: 86px 0 0 40px;
    position: relative;
  }
  .person-name {
    font-family: "Montserrat", Arial, sans-serif;
    font-weight: 700;
    color: var(--white);
    font-size: 30px;
    line-height: 1;
  }
  .person-role {
    color: #022e02;
    font-size: 20px;
    margin-top: 4px;
  }
  .rule {
    margin-top: 10px;
    height: 2px;
    background: var(--green-line);
    width: 100%;
  }
  .contacts {
    position: absolute;
    left: 40px;
    bottom: 28px;
    list-style: none;
  }
  .contacts li {
    display: flex;
    align-items: center;
    gap: 12px;
    color: var(--white);
    font-size: 17px;
    line-height: 1;
    margin-top: 10px;
  }
  .contacts svg { width: 22px; height: 20px; flex: none; }

  .back-brand {
    flex: 1;
    background: var(--green-bright);
    position: relative;
    display: flex;
    align-items: center;
    justify-content: center;
  }
  .back-brand .brand-name { font-size: 34px; text-align: center; padding: 0 24px 40px; }
  .social {
    position: absolute;
    right: 22px;
    bottom: 24px;
    display: flex;
    align-items: center;
    gap: 8px;
  }
  .social-dot { width: 18px; height: 18px; background: #089c08; }
  .social-handle { margin-left: 6px; font-size: 19px; color: var(--green-deep); }
</style>
</head>
<body>
  <section class="card card-front">
    <div class="portrait" role="img" aria-label="Photo of the trainer kneeling outdoors with his shepherd dog"></div>
    <div class="front-brand">
      <div class="brand-seal">
        <span class="brand-name">Pine Ridge Canine Coaching</span>
      </div>
    </div>
  </section>

  <section class="card card-back">
    <div class="back-info">
      <h1 class="person-name">Trevor Holloway</h1>
      <p class="person-role">dog trainer</p>
      <div class="rule"></div>
      <ul class="contacts">
        <li>
          <svg viewBox="0 0 22 20" aria-hidden="true"><rect width="22" height="20" fill="#00d200"/><path d="M7 5c1 0 2 2 2 3s-1 1-1 2 2 3 3 3 1-1 2-1 3 1 3 2-1 2-2 2C9 16 6 12 6 8c0-2 0-3 1-3z" fill="#036d03"/></svg>
          555-304-7162
        </li>
        <li>
          <svg viewBox="0 0 22 20" aria-hidden="true"><rect width="22" height="20" fill="#00d200"/><rect x="5" y="6" width="12" height="8" fill="none" stroke="#036d03" stroke-width="1.5"/><path d="M5 6l6 5 6-5" fill="none" stroke="#036d03" stroke-width="1.5"/></svg>
          info@pineridgecanine.example
        </li>
        <li>
          <svg viewBox="0 0 22 20" aria-hidden="true"><rect width="22" height="20" fill="#00d200"/><circle cx="11" cy="10" r="6" fill="none" stroke="#036d03" stroke-width="1.4"/><ellipse cx="11" cy="10" rx="2.5" ry="6" fill="none" stroke="#036d03" stroke-width="1.2"/><path d="M5 10h12" stroke="#036d03" stroke-width="1.2"/></svg>
          www.pineridgecanine.example
        </li>
      </ul>
    </div>
    <div class="back-brand">
      <span class="brand-name">Pine Ridge Canine Coaching</span>
      <div class="social">
        <span class="social-dot"></span>
        <span class="social-dot"></span>
        <span class="social-dot"></span>
        <span class="social-handle">pineridgecanine</span>
      </div>
    </div>
  </section>
</body>
</html>
```